Wedding invitation

Hello,

I would like the same attached image in a vertical rectangular 3D effect design, same colours,
but without text.

I would like eaxctly like the attachment design, in a long vertical, ration 16:9 size for social media.

```html
<!DOCTYPE html>
<html lang="en">
<head>
<meta charset="utf-8">
<title>Wedding Invitation Frame</title>
<link rel="stylesheet" href="https://fonts.googleapis.com/css2?family=Open+Sans:wght@400&display=swap">
<style>
  :root {
    --navy: #2b3547;
    --navy-deep: #1f2735;
    --navy-edge: #141a24;
    --moulding: #2e384a;
    --gold-light: #f4c266;
    --gold: #d98f26;
    --gold-dark: #a8661a;
    --ink-light: #ffffff;
  }
  html, body {
    margin: 0;
    padding: 0;
    width: 706px;
    height: 1200px;
    overflow: hidden;
    background: var(--navy);
  }
  .invitation {
    position: relative;
    width: 706px;
    height: 1200px;
    background: radial-gradient(ellipse at 50% 45%, #303b4f 0%, var(--navy) 55%, #283142 100%);
    overflow: hidden;
  }
  .panel-frames {
    position: absolute;
    inset: 0;
    width: 706px;
    height: 1200px;
  }
  .moulding-outer { fill: var(--moulding); stroke: var(--navy-edge); stroke-width: 3; }
  .moulding-middle { fill: var(--navy-deep); stroke: #3a4559; stroke-width: 2; }
  .moulding-inner { fill: var(--navy); stroke: var(--navy-edge); stroke-width: 3; }
  .gold-trim { fill: none; stroke: url(#goldSheen); stroke-width: 17; stroke-linejoin: miter; }
  .gold-highlight { fill: none; stroke: rgba(255, 236, 180, 0.35); stroke-width: 3; }
  .ratio-label {
    position: absolute;
    left: 0;
    right: 0;
    top: 586px;
    margin: 0;
    text-align: center;
    font-family: "Open Sans", sans-serif;
    font-size: 21px;
    font-weight: 400;
    color: var(--ink-light);
    letter-spacing: 0.5px;
  }
</style>
</head>
<body>
  <main class="invitation">
    <svg class="panel-frames" viewBox="0 0 706 1200" xmlns="http://www.w3.org/2000/svg" aria-hidden="true">
      <defs>
        <linearGradient id="goldSheen" x1="0" y1="0" x2="1" y2="1">
          <stop offset="0" stop-color="var(--gold-light)"/>
          <stop offset="0.35" stop-color="var(--gold)"/>
          <stop offset="0.6" stop-color="var(--gold-light)"/>
          <stop offset="1" stop-color="var(--gold-dark)"/>
        </linearGradient>
        <filter id="raisedShadow" x="-10%" y="-10%" width="120%" height="120%">
          <feDropShadow dx="-4" dy="4" stdDeviation="5" flood-color="#05080d" flood-opacity="0.7"/>
        </filter>
        <filter id="goldShadow" x="-10%" y="-10%" width="120%" height="120%">
          <feDropShadow dx="-2" dy="3" stdDeviation="2.5" flood-color="#05080d" flood-opacity="0.6"/>
        </filter>
      </defs>

      <path class="moulding-outer" filter="url(#raisedShadow)"
        d="M48,116 L92,116 Q100,116 100,108 Q136,98 148,68 Q158,46 183,46 L523,46 Q548,46 558,68 Q570,98 606,108 Q606,116 614,116 L658,116 L658,1087 L614,1087 Q606,1087 606,1095 Q570,1105 558,1135 Q548,1157 523,1157 L183,1157 Q158,1157 148,1135 Q136,1105 100,1095 Q100,1087 92,1087 L48,1087 Z"/>
      <path class="moulding-middle"
        d="M60,128 L100,128 Q110,128 110,118 Q146,108 158,80 Q166,58 190,58 L516,58 Q540,58 548,80 Q560,108 596,118 Q596,128 606,128 L646,128 L646,1075 L606,1075 Q596,1075 596,1085 Q560,1095 548,1123 Q540,1145 516,1145 L190,1145 Q166,1145 158,1123 Q146,1095 110,1085 Q110,1075 100,1075 L60,1075 Z"/>
      <path class="moulding-inner" filter="url(#raisedShadow)"
        d="M72,140 L108,140 Q118,140 118,130 Q154,120 166,92 Q174,70 198,70 L508,70 Q532,70 540,92 Q552,120 588,130 Q588,140 598,140 L634,140 L634,1063 L598,1063 Q588,1063 588,1073 Q552,1083 540,1111 Q532,1133 508,1133 L198,1133 Q174,1133 166,1111 Q154,1083 118,1073 Q118,1063 108,1063 L72,1063 Z"/>

      <path class="gold-trim" filter="url(#goldShadow)"
        d="M109,175 L145,152 L178,150 Q183,113 205,113 L501,113 Q523,113 528,150 L561,152 L597,175 L597,1028 L561,1051 L528,1053 Q523,1090 501,1090 L205,1090 Q183,1090 178,1053 L145,1051 L109,1028 Z"/>
      <path class="gold-highlight"
        d="M105,175 L143,149 L175,147 Q181,109 205,109 L501,109"/>
    </svg>

    <p class="ratio-label">16 : 9</p>
  </main>
</body>
</html>
```